Business Card Design Project

Looking for a simple and stylish business card. We are an Advertising Company. The card Must feature the company logo (attached) and also this info.
p: 0481629054
e: sales@rv-promo.com.au
w: www.rv-promo.com.au
We Advertise mainly using TV screens featured in restaurants and cafe. See website for more about the business.
Not really looking for a plain background, but at the same time do not want to much happening in the Background. I am not really to fussy though with the design or the colour scheme, and I am leaving the creativity part up to you creative designers.

```html
<!DOCTYPE html>
<html lang="en">
<head>
<meta charset="utf-8">
<title>RV Promo – Business Card</title>
<link href="https://fonts.googleapis.com/css2?family=Oswald:wght@300;400&display=swap" rel="stylesheet">
<style>
  :root {
    --backdrop: #e6e3df;
    --card-black: #111113;
    --card-black-soft: #1b1b1f;
    --pink: #e8246a;
    --purple: #8a4aa8;
    --blue: #3050b4;
    --white: #ffffff;
    --brand-gradient: linear-gradient(90deg, var(--pink) 0%, var(--purple) 55%, var(--blue) 100%);
  }
  * { box-sizing: border-box; margin: 0; padding: 0; }
  html, body {
    width: 1200px;
    height: 751px;
    overflow: hidden;
    background: var(--backdrop);
  }
  .stage {
    position: relative;
    width: 1200px;
    height: 751px;
    display: flex;
    align-items: center;
    justify-content: center;
    gap: 48px;
  }
  .card {
    position: relative;
    width: 520px;
    height: 300px;
    overflow: hidden;
    background: radial-gradient(ellipse at 50% 40%, var(--card-black-soft) 0%, var(--card-black) 75%);
    box-shadow: 0 6px 18px rgba(0,0,0,0.25);
    font-family: "Oswald", sans-serif;
  }

  /* Front */
  .card-front__band {
    position: absolute;
    top: 0; left: 0; right: 0;
    height: 20px;
    background: var(--brand-gradient);
  }
  .brand-name {
    font-family: "Oswald", sans-serif;
    font-weight: 300;
    color: var(--pink);
    letter-spacing: 2px;
    white-space: nowrap;
  }
  .card-front__name {
    position: absolute;
    top: 34px;
    left: 224px;
    font-size: 32px;
    line-height: 1.2;
  }
  .contact-list {
    position: absolute;
    top: 88px;
    left: 224px;
    list-style: none;
  }
  .contact-list__item {
    display: flex;
    align-items: center;
    gap: 12px;
    height: 40px;
    color: var(--white);
    font-size: 19px;
    font-weight: 400;
    line-height: 1;
    text-transform: uppercase;
    letter-spacing: 0.5px;
  }
  .contact-list__icon {
    width: 20px;
    height: 20px;
    flex: none;
  }
  .card-front__watermark {
    position: absolute;
    left: 10px;
    bottom: -8px;
    font-size: 86px;
    line-height: 0.8;
    opacity: 0.28;
    letter-spacing: 4px;
  }

  /* Back */
  .card-back__side-bar {
    position: absolute;
    top: 0; right: 0; bottom: 0;
    width: 20px;
    background: linear-gradient(180deg, var(--blue) 0%, var(--purple) 50%, var(--pink) 100%);
  }
  .card-back__pattern {
    position: absolute;
    top: -60px;
    left: -10px;
    width: 280px;
    height: 230px;
    background: radial-gradient(closest-side, rgba(200,60,120,0.8) 0%, rgba(170,50,105,0.45) 50%, rgba(17,17,19,0) 100%);
  }
  .card-back__name {
    position: absolute;
    top: 138px;
    left: 228px;
    font-size: 40px;
    line-height: 1.2;
  }
  .card-back__rule {
    position: absolute;
    top: 212px;
    left: 0;
    right: 34px;
    height: 3px;
    background: linear-gradient(90deg, var(--blue) 0%, var(--purple) 50%, var(--pink) 100%);
  }
</style>
</head>
<body>
<main class="stage">

  <section class="card card-front" aria-label="Business card front">
    <div class="card-front__band"></div>
    <div class="brand-name card-front__name">RV PROMO</div>

    <ul class="contact-list">
      <li class="contact-list__item">
        <svg class="contact-list__icon" viewBox="0 0 24 24" aria-hidden="true">
          <path fill="#fff" d="M6.6 10.8a15.1 15.1 0 0 0 6.6 6.6l2.2-2.2c.3-.3.7-.4 1-.2 1.1.4 2.3.6 3.6.6.6 0 1 .4 1 1V20c0 .6-.4 1-1 1A17 17 0 0 1 3 4c0-.6.4-1 1-1h3.5c.6 0 1 .4 1 1 0 1.3.2 2.5.6 3.6.1.3 0 .7-.2 1z"/>
        </svg>
        <span>0481629054</span>
      </li>
      <li class="contact-list__item">
        <svg class="contact-list__icon" viewBox="0 0 24 24" aria-hidden="true">
          <rect x="3" y="6" width="18" height="12" fill="#fff"/>
          <path d="M3 6l9 7 9-7" fill="none" stroke="#111113" stroke-width="1.5"/>
        </svg>
        <span>sales@rv-promo.com.au</span>
      </li>
      <li class="contact-list__item">
        <svg class="contact-list__icon" viewBox="0 0 24 24" aria-hidden="true">
          <circle cx="12" cy="12" r="9" fill="none" stroke="#fff" stroke-width="2"/>
          <path d="M3 12h18M12 3c3 3 3 15 0 18M12 3c-3 3-3 15 0 18" fill="none" stroke="#fff" stroke-width="1.5"/>
        </svg>
        <span>www.rv-promo.com.au</span>
      </li>
    </ul>

    <div class="brand-name card-front__watermark" aria-hidden="true">RV PROMO</div>
  </section>

  <section class="card card-back" aria-label="Business card back">
    <div class="card-back__pattern" role="img" aria-label="Cluster of pink hexagon shapes in the top left corner"></div>
    <div class="brand-name card-back__name">RV PROMO</div>
    <div class="card-back__rule"></div>
    <div class="card-back__side-bar"></div>
  </section>

</main>
</body>
</html>
```